Business card design for a engineering company

I need a double sided business card design for my company "Verdmont Flow Solutions". The card will be used in Malaysia. Sleek and professional, with a little design flare to it.
Information to showcase:
1. Company logo
2. Name, title, phone, email address, website address
3. our products "Pumping technology, Valve & actuation, Air Moving Technology
Example:
Ravi Tanaka
Business manager
ravi.tanaka@verdmont-example.com
www.verdmont-example.com.my
- Pumping technology
- Valve & actuation
- Air moving technology
Target Market(s)
engineers, purchasing managers
Industry/Entity Type
Business
Contact Information for Business Card
Ravi Tanaka
Business manager
ravi.tanaka@verdmont-example.com
www.verdmont-example.com.my
- Pumping technology
- Valve & actuation
- Air moving technology
catch phrase : "Solving flow challenges, exceeding expectations"

```html
<!DOCTYPE html>
<html lang="en">
<head>
<meta charset="utf-8">
<title>Verdmont Flow Solutions – Business Card</title>
<link href="https://fonts.googleapis.com/css2?family=Lato:wght@400;700;900&display=swap" rel="stylesheet">
<style>
  :root {
    --teal: #0e3446;
    --teal-ink: #163c4e;
    --orange: #f5a01a;
    --orange-deep: #f08a12;
    --paper: #ffffff;
    --stage: #e6e8ea;
  }
  * { box-sizing: border-box; margin: 0; padding: 0; }
  html, body { width: 1200px; height: 900px; overflow: hidden; }
  body {
    background: var(--stage);
    font-family: "Lato", Arial, sans-serif;
    position: relative;
  }
  .card {
    position: absolute;
    left: 320px;
    width: 560px;
    height: 320px;
    overflow: hidden;
    box-shadow: 0 6px 18px rgba(0,0,0,0.18);
  }
  /* Back side */
  .card--back { top: 100px; background: var(--teal); color: var(--paper); }
  .brand-lockup {
    position: absolute; left: 0; right: 0; top: 96px;
    display: flex; justify-content: center; align-items: center; gap: 14px;
  }
  .brand-dot { width: 30px; height: 30px; border-radius: 50%; background: var(--paper); flex: none; }
  .brand-name { font-weight: 700; font-size: 30px; letter-spacing: 1px; white-space: nowrap; }
  .tagline {
    position: absolute; left: 0; right: 0; top: 150px;
    text-align: center; font-size: 13px; letter-spacing: 0.3px; color: var(--paper);
  }
  .product-list {
    position: absolute; left: 28px; right: 28px; bottom: 30px;
    list-style: none; display: flex; justify-content: space-between;
    font-size: 14px; letter-spacing: 0.3px;
  }
  .product-list li::before { content: "•"; margin-right: 7px; }

  /* Front side */
  .card--front { top: 480px; background: var(--paper); }
  .card-art { position: absolute; inset: 0; width: 560px; height: 320px; }
  .front-brand {
    position: absolute; left: 80px; top: 40px;
    display: flex; align-items: center; gap: 10px;
  }
  .front-brand .brand-dot { width: 24px; height: 24px; background: var(--teal); }
  .front-brand .brand-name { font-size: 22px; color: var(--teal); }
  .holder { position: absolute; left: 40px; top: 242px; }
  .holder-name { font-weight: 900; font-size: 40px; color: var(--teal-ink); line-height: 1; }
  .holder-title { font-size: 18px; color: var(--orange); margin-top: 3px; }
  .contact-list {
    position: absolute; left: 300px; top: 160px; list-style: none;
    font-size: 12.5px; color: var(--teal-ink);
  }
  .contact-list li { display: flex; align-items: center; gap: 8px; margin-bottom: 9px; }
  .contact-list svg { width: 13px; height: 13px; flex: none; }
</style>
</head>
<body>

<section class="card card--back" aria-label="Card back">
  <div class="brand-lockup">
    <span class="brand-dot"></span>
    <span class="brand-name">Verdmont Flow Solutions</span>
  </div>
  <p class="tagline">Solving flow challenges, exceeding expectations</p>
  <ul class="product-list">
    <li>Pumping technology</li>
    <li>Valve &amp; actuation</li>
    <li>Air moving technology</li>
  </ul>
</section>

<section class="card card--front" aria-label="Card front">
  <svg class="card-art" viewBox="0 0 560 320">
    <defs>
      <linearGradient id="texture-fill" x1="0" y1="0" x2="1" y2="1">
        <stop offset="0" stop-color="#f1f1f1"/>
        <stop offset="1" stop-color="#e4e4e4"/>
      </linearGradient>
    </defs>
    <path role="img" aria-label="Fine diagonal line texture" d="M0 0 H560 V66 C520 70 460 78 380 95 C260 120 120 180 0 250 Z" fill="url(#texture-fill)"/>
    <path class="curve-main" d="M0 250 C120 180 260 120 380 95 C460 78 520 70 560 66" fill="none" stroke="#f5a01a" stroke-width="6"/>
    <path class="curve-accent" d="M420 80 C470 68 515 60 552 56" fill="none" stroke="#f08a12" stroke-width="3" stroke-linecap="round"/>
  </svg>

  <div class="front-brand">
    <span class="brand-dot"></span>
    <span class="brand-name">Verdmont Flow Solutions</span>
  </div>

  <ul class="contact-list">
    <li>
      <svg viewBox="0 0 16 16"><path d="M3 1l3 3-2 2c1 2 3 4 5 5l2-2 3 3-2 3C6 15 1 10 1 3z" fill="#f5a01a"/></svg>
      +60 3 5550 1482
    </li>
    <li>
      <svg viewBox="0 0 16 16"><rect x="1" y="3" width="14" height="10" fill="#f5a01a"/><path d="M1 3l7 6 7-6" fill="none" stroke="#fff" stroke-width="1.4"/></svg>
      ravi.tanaka@verdmont-example.com
    </li>
    <li>
      <svg viewBox="0 0 16 16"><circle cx="8" cy="8" r="7" fill="#f5a01a"/><path d="M1 8h14M8 1c-3 3-3 11 0 14M8 1c3 3 3 11 0 14" fill="none" stroke="#fff" stroke-width="1"/></svg>
      www.verdmont-example.com.my
    </li>
  </ul>

  <div class="holder">
    <h1 class="holder-name">Ravi Tanaka</h1>
    <p class="holder-title">Business Manager</p>
  </div>
</section>

</body>
</html>
```